Postcard Design

The business Logo is 'Verdo' it is grass cutting and maintenance. It will offer grass cutting with stripes including edging. Other services include decking/fencing maintenance, lawn treatment and patio/drive cleaning...... prices start from £10 to include front and rear lawns, Regular cuts or a one off tidy. private and commercial. Contracts welcome.
call 01642583106 or 07474829150 for a free quote.
one of the pics that i have sent is the logo (obviously it would need to be tidied up and neater) that is just rough. The other pic is one of pella cards templates but is the one that is the preferred out of all of them. If it could be similar to that with the logo on would be great.
a before (long scruffy grass) and after (neat Lawn) half and half of the postcard would be great.

Target Market(s)

Middle class home owners.

Industry/Entity Type

Business

Requirements
Must have
• The 'Verdo' logo
Nice to have
• we have a lot of junk mail posted in this area and a lot just gets put in the bin so could you make it eye catching.

```html
<!DOCTYPE html>
<html lang="en">
<head>
<meta charset="utf-8">
<title>Verdo Postcard</title>
<link rel="stylesheet" href="https://fonts.googleapis.com/css2?family=Archivo+Black&family=Arimo:wght@700&display=swap">
<style>
  :root {
    --bg: #000000;
    --card-white: #ffffff;
    --band-green: #6a9a3a;
    --grass-light: #8cc152;
    --grass-mid: #6fa63a;
    --grass-dark: #4f7f26;
    --ink: #111111;
    --text-white: #ffffff;
  }
  html, body {
    margin: 0;
    padding: 0;
    width: 1200px;
    height: 1047px;
    overflow: hidden;
    background: var(--bg);
  }
  .canvas {
    position: relative;
    width: 1200px;
    height: 1047px;
    background: var(--bg);
    overflow: hidden;
  }

  /* Back of postcard, laid at a slight angle */
  .card-back {
    position: absolute;
    left: 115px;
    top: 190px;
    width: 740px;
    height: 571px;
    background: var(--card-white);
    transform-origin: 0 0;
    transform: rotate(-10deg);
  }
  .card-back .grass-band {
    position: absolute;
    left: 0;
    top: 0;
    width: 560px;
    height: 185px;
    background:
      radial-gradient(ellipse at 50% 0%, rgba(255,255,255,0.14), transparent 60%),
      linear-gradient(180deg, var(--grass-mid), var(--grass-light) 45%, var(--grass-mid) 80%, var(--grass-dark));
  }
  .card-back .brand-name {
    position: absolute;
    left: 0;
    width: 560px;
    top: 62px;
    text-align: center;
    font-family: "Archivo Black", sans-serif;
    font-size: 72px;
    line-height: 1;
    color: var(--ink);
    letter-spacing: 2px;
  }
  .card-back .call-line {
    position: absolute;
    left: 0;
    width: 560px;
    top: 148px;
    text-align: center;
    font-family: "Arimo", sans-serif;
    font-weight: 700;
    font-size: 17px;
    color: var(--ink);
  }

  /* Front of postcard */
  .card-front {
    position: absolute;
    left: 357px;
    top: 393px;
    width: 738px;
    height: 562px;
    overflow: hidden;
    background:
      radial-gradient(ellipse at 50% 30%, rgba(255,255,255,0.14), transparent 65%),
      linear-gradient(180deg, var(--grass-light), var(--grass-mid) 60%, var(--grass-dark));
  }
  .card-front .services-band {
    position: absolute;
    left: 0;
    top: 0;
    width: 100%;
    height: 124px;
    background: var(--band-green);
    display: flex;
    flex-direction: column;
    justify-content: center;
    align-items: center;
    gap: 3px;
    font-family: "Arimo", sans-serif;
    font-weight: 700;
    font-size: 24px;
    line-height: 28px;
    letter-spacing: 0.4px;
    color: var(--text-white);
    text-align: center;
    text-shadow: 0 1px 2px rgba(0,0,0,0.35);
  }
  .card-front .price-headline {
    position: absolute;
    left: 0;
    width: 100%;
    top: 161px;
    text-align: center;
    font-family: "Archivo Black", sans-serif;
    font-size: 38px;
    line-height: 1;
    color: var(--ink);
    letter-spacing: 2px;
  }
  .card-front .price-sub {
    position: absolute;
    left: 0;
    width: 100%;
    top: 205px;
    text-align: center;
    font-family: "Archivo Black", sans-serif;
    font-size: 28px;
    line-height: 1;
    color: var(--ink);
    letter-spacing: 0.5px;
  }
  .card-front .brand-name {
    position: absolute;
    left: 0;
    width: 100%;
    top: 300px;
    text-align: center;
    font-family: "Archivo Black", sans-serif;
    font-size: 120px;
    line-height: 1;
    color: var(--ink);
    letter-spacing: 4px;
  }
  .card-front .contact-band {
    position: absolute;
    left: 0;
    bottom: 0;
    width: 100%;
    height: 98px;
    background: var(--band-green);
    display: flex;
    flex-direction: column;
    justify-content: center;
    align-items: center;
    color: var(--text-white);
    text-shadow: 0 1px 2px rgba(0,0,0,0.35);
  }
  .card-front .contracts {
    font-family: "Archivo Black", sans-serif;
    font-size: 33px;
    line-height: 36px;
    letter-spacing: 1px;
  }
  .card-front .call-line {
    font-family: "Arimo", sans-serif;
    font-weight: 700;
    font-size: 23px;
    line-height: 28px;
    letter-spacing: 1px;
  }
</style>
</head>
<body>
<div class="canvas">

  <section class="card-back">
    <div class="grass-band" role="img" aria-label="Photograph of a freshly mown striped lawn"></div>
    <div class="brand-name">VERDO</div>
    <div class="call-line">Call 01642583106 or 07474829150 for a free quote!</div>
  </section>

  <section class="card-front" role="img" aria-label="Photograph of a freshly mown striped lawn">
    <div class="services-band">
      <div>GRASS CUTTING WITH STRIPES INCLUDING EDGING</div>
      <div>DECKING/FENCING MAINTENANCE</div>
      <div>LAWN TREATMENT &amp; PATIO/DRIVE CLEANING</div>
    </div>
    <div class="price-headline">PRICES START FROM £10</div>
    <div class="price-sub">TO INCLUDE FRONT AND REAR LAWNS!</div>
    <div class="brand-name">VERDO</div>
    <div class="contact-band">
      <div class="contracts">CONTRACTS WELCOME!</div>
      <div class="call-line">Call 01642583106 or 07474829150 for a free quote!</div>
    </div>
  </section>

</div>
</body>
</html>
```